Bref créative
Business Cards and Stationery For Bright Harbour Trails
Bright Harbour Trails
Professional
Tom Whitlock
***No address to be printed***
tom@brightharbourtrails.co.uk
www.brightharbourtrails.co.uk
I have attached two different logos that I like for you to play with for the design of my business card and stationery. Ultimately, I want to give an impression of elegance and sophistication. I am happy for you to play with the colours and I will give as much feedback as I can to help guide you. Please ask me any questions that you wish to.
Please note that I will ask the winning designer to do a second version with .com, as well as the .co.uk that I have asked you to do.
The logo with strapline.

```html
<!DOCTYPE html>
<html lang="en">
<head>
<meta charset="utf-8">
<title>Bright Harbour Trails – Business Card</title>
<link href="https://fonts.googleapis.com/css2?family=Cinzel:wght@600&family=Cormorant+Garamond:ital,wght@0,500;1,500&display=swap" rel="stylesheet">
<style>
  :root {
    --bg: #e9e6e1;
    --gold-light: #e8d49a;
    --gold: #c9a95a;
    --gold-deep: #9c7a2f;
    --cream: #fffdf7;
    --ink-green: #4a7a2a;
    --text-gold: #a8853a;
    --text-grey: #6d6658;
  }
  * { margin: 0; padding: 0; box-sizing: border-box; }
  html, body { width: 1200px; height: 864px; overflow: hidden; background: var(--bg); }
  .canvas { position: relative; width: 1200px; height: 864px; }

  .card {
    position: absolute; width: 540px; height: 310px; border-radius: 16px;
    overflow: hidden; box-shadow: 0 8px 24px rgba(0,0,0,.18);
  }

  /* Front */
  .card-front {
    left: 40px; top: 130px;
    background: radial-gradient(ellipse at 30% 35%, var(--gold-light) 0%, var(--gold) 50%, var(--gold-deep) 100%);
  }
  .front-illustration {
    position: absolute; left: 26px; top: 120px; width: 250px; height: 170px;
    background: linear-gradient(180deg, #fbf6e6 0%, #f1e6c2 100%);
    border-radius: 6px 6px 0 0;
  }
  .front-brand { position: absolute; left: 290px; top: 78px; width: 230px; text-align: center; }
  .brand-name {
    font-family: "Cinzel", serif; font-weight: 600; color: var(--cream);
    font-size: 27px; line-height: 1.05; letter-spacing: 1px;
  }
  .strapline {
    font-family: "Cormorant Garamond", serif; font-style: italic; font-weight: 500;
    color: var(--cream); font-size: 24px; margin-top: 6px;
  }

  /* Back */
  .card-back { left: 620px; top: 420px; background: var(--cream); }
  .back-swoosh { position: absolute; left: 0; top: 0; width: 540px; height: 310px; }
  .holder-name {
    position: absolute; right: 28px; top: 112px;
    font-family: "Cinzel", serif; font-weight: 600; font-size: 10px;
    letter-spacing: 1.5px; color: var(--text-gold); text-transform: uppercase;
  }
  .back-brand { position: absolute; left: 24px; top: 150px; display: flex; align-items: flex-end; gap: 10px; }
  .back-illustration {
    width: 80px; height: 64px; border-radius: 4px;
    background: linear-gradient(180deg, #e7d69c 0%, #7fa84e 100%);
  }
  .back-brand .brand-name { color: var(--ink-green); font-size: 20px; }
  .back-brand .strapline { color: var(--text-gold); font-size: 17px; margin-top: 2px; }
  .contact-list {
    position: absolute; left: 26px; bottom: 20px; list-style: none;
    font-family: "Cormorant Garamond", serif; font-weight: 500; font-size: 11px;
    color: var(--text-grey); line-height: 1.45;
  }
  .contact-list li { display: flex; align-items: center; gap: 6px; }
  .contact-list svg { width: 9px; height: 9px; fill: var(--text-gold); }
</style>
</head>
<body>
<main class="canvas">

  <section class="card card-front" aria-label="Business card front">
    <div class="front-illustration" role="img" aria-label="Cream line illustration of a gothic cathedral facade"></div>
    <div class="front-brand">
      <div class="brand-name">BRIGHT HARBOUR TRAILS</div>
      <div class="strapline">Tailor made for you</div>
    </div>
  </section>

  <section class="card card-back" aria-label="Business card back">
    <svg class="back-swoosh" viewBox="0 0 540 310" aria-hidden="true">
      <defs>
        <linearGradient id="swooshGold" x1="0" y1="0" x2="1" y2="0">
          <stop offset="0" stop-color="#e8d49a"/>
          <stop offset=".55" stop-color="#c9a95a"/>
          <stop offset="1" stop-color="#9c7a2f"/>
        </linearGradient>
      </defs>
      <path d="M0 0 H540 V58 C420 40 300 70 200 110 C120 142 50 170 0 200 Z" fill="url(#swooshGold)"/>
      <path d="M0 214 C70 170 160 130 260 104 C360 80 450 78 540 92" fill="none" stroke="#c9a95a" stroke-width="2"/>
    </svg>
    <div class="holder-name">Tom Whitlock</div>
    <div class="back-brand">
      <div class="back-illustration" role="img" aria-label="Small illustration of a cathedral with green trees"></div>
      <div>
        <div class="brand-name">BRIGHT HARBOUR TRAILS</div>
        <div class="strapline">Tailor made for you</div>
      </div>
    </div>
    <ul class="contact-list">
      <li><svg viewBox="0 0 10 10"><path d="M2 0h2l1 3-1.5 1a6 6 0 0 0 2.5 2.5L7 5l3 1v2c0 1-1 2-2 2A8 8 0 0 1 0 2c0-1 1-2 2-2z"/></svg>01632 960481</li>
      <li><svg viewBox="0 0 10 10"><rect x="2" y="0" width="6" height="10" rx="1.2"/></svg>07700 900317</li>
      <li><svg viewBox="0 0 10 10"><path d="M0 2h10v6H0z M0 2l5 3.5L10 2" /></svg>tom@brightharbourtrails.co.uk</li>
      <li><svg viewBox="0 0 10 10"><circle cx="5" cy="5" r="5"/></svg>www.brightharbourtrails.co.uk</li>
    </ul>
  </section>

</main>
</body>
</html>
```